Envelope and Stationary

I need an envelope and stationary package for my non-profit. I need to be able to download these, print, and use.

I am attached the logos, color files, and information I want on envelope and stationary.

The letter must have room on the left margin to put the list of names, Board Members, etc... I will attach a sample.

What I am looking for is to jazz this up a little bit. The Corla Penwick Children's Foundation is promotes physical fitness in children through after school programs.

Once this project is done, I need a powerpoint template, business cards, and many other pieces.

Please help me make my envelopes and letterhead standout from everyone else.

Target Market(s)

Donors, Community citizens, and prospective partners.

Industry/Entity Type

Fitness

Requirements
Must have
• 1) Logo - see attached
2) Mission Statement - "The MISSION of the CORLA PENWICK FOUNDATION is to provide after school enrichment, health, and fitness programs in a safe and nurturing environment."
3) Contact information
4) Space on left Margin for Board of Directors (this space will be available for edits to add/subtract names).

5) See sample letter head: The logo and address is too small and barely visible.

6) PO BOX 371924 * Alder Springs, Oregon 32917
Phone: 877-(CPF)-2315
Email: community@cpfyouth.org
Web: www.cpfyouth.org
Nice to have
• Logo and colors have some feel or scheme across top. Something that makes the letterhead and envelope stand out.

```html
<!DOCTYPE html>
<html lang="en">
<head>
<meta charset="utf-8">
<title>Corla Penwick Children's Foundation – Stationery</title>
<link rel="stylesheet" href="https://fonts.googleapis.com/css2?family=Arimo:wght@400;700&family=Roboto+Condensed:wght@400&display=swap">
<style>
  :root{
    --brand-blue:#1f4e9e;
    --brand-red:#c4202f;
    --wine:#7a1520;
    --paper:#ffffff;
    --ink:#1b1b1b;
    --stage:#d9d6d2;
    --rule:#9a9a9a;
  }
  *{box-sizing:border-box;margin:0;padding:0}
  html,body{width:1200px;height:900px;overflow:hidden}
  body{background:var(--stage);position:relative;font-family:"Arimo",Arial,sans-serif;color:var(--ink)}
  .icon-defs{position:absolute;width:0;height:0}

  /* shared */
  .sheet{position:absolute;background:var(--paper);overflow:hidden;box-shadow:0 3px 10px rgba(0,0,0,.25)}
  .wordmark{display:flex;align-items:center;gap:8px}
  .wordmark__square{background:var(--brand-red);flex:none}
  .wordmark__name{font-family:"Arimo",Arial,sans-serif;font-weight:700;color:var(--brand-blue);text-transform:uppercase;line-height:1.05}
  .footer-band{position:absolute;left:0;right:0;bottom:0}
  .footer-band svg.swoosh{position:absolute;inset:0;width:100%;height:100%}
  .contact{position:absolute;font-family:"Roboto Condensed","Arial Narrow",sans-serif;color:#fff;display:flex;flex-direction:column}
  .contact__line{display:flex;align-items:center;white-space:nowrap}
  .contact__line svg{fill:#fff;flex:none}

  /* letterhead back sheet */
  .letter-back{position:absolute;left:17px;top:21px;width:576px;height:743px;background:var(--brand-blue);box-shadow:0 3px 10px rgba(0,0,0,.25)}

  /* letterhead */
  .letterhead{left:65px;top:128px;width:575px;height:745px}
  .letterhead .wordmark{position:absolute;left:20px;top:34px}
  .letterhead .wordmark__square{width:44px;height:44px}
  .letterhead .wordmark__name{font-size:19px}
  .letterhead__mission{position:absolute;left:152px;top:98px;width:400px;font-size:4.6px;white-space:nowrap}
  .board{position:absolute;left:22px;top:155px;width:55px;height:320px;border-right:1px solid var(--rule);font-size:4.3px;line-height:6.5px}
  .board__title{font-weight:700;font-size:5.4px;margin-bottom:3px}
  .board__list{list-style:none}
  .board__list li::before{content:"• "}
  .letter{position:absolute;left:118px;top:187px;width:420px;font-size:7.1px;line-height:9.1px}
  .letter .letter__subject{width:420px;text-align:center;font-size:9.6px;font-weight:700;margin-bottom:26px}
  .letter p{width:420px;margin-bottom:9px}
  .letter .letter__paragraph--joined{margin-top:-9px}
  .letter .letter__closing{margin-top:26px}
  .letter .letter__signer{margin-top:18px;font-size:9.6px;line-height:10px}
  .letter__signer small{display:block;font-size:7.1px}
  .letterhead .footer-band{height:137px}
  .letterhead .contact{left:52px;top:60px;font-size:12.5px;gap:3px}
  .letterhead .contact svg{width:14px;height:14px;margin-right:8px}
  .letterhead .contact--web{left:408px;top:74px}

  /* envelope */
  .envelope-back{position:absolute;left:683px;top:33px;width:445px;height:197px;background:var(--paper);box-shadow:0 3px 10px rgba(0,0,0,.25);overflow:hidden}
  .envelope-back__flap{position:absolute;left:0;top:0;width:100%;height:58px}
  .envelope{left:711px;top:185px;width:466px;height:207px}
  .envelope .wordmark{position:absolute;left:12px;top:20px}
  .envelope .wordmark__square{width:30px;height:30px}
  .envelope .wordmark__name{font-size:12px}
  .envelope__window{position:absolute;left:249px;top:35px;width:191px;height:57px;border:1px solid #cfcfcf;border-radius:8px;background:linear-gradient(#fafafa,#e9e9e9)}
  .envelope .footer-band{height:90px}
  .envelope .contact{left:18px;top:40px;font-size:8.6px;gap:2px}
  .envelope .contact svg{width:10px;height:10px;margin-right:6px}
  .envelope .contact--web{left:360px;top:48px}

  /* business card back */
  .card-back{position:absolute;left:681px;top:454px;width:338px;height:193px;background:var(--wine);box-shadow:0 3px 10px rgba(0,0,0,.25)}
  .card-back__mission{position:absolute;left:0;right:0;top:158px;text-align:center;color:#fff;font-family:"Roboto Condensed","Arial Narrow",sans-serif;font-size:7.2px;line-height:9.5px}

  /* business card front */
  .card{left:800px;top:666px;width:374px;height:212px}
  .card .wordmark{position:absolute;left:26px;top:22px}
  .card .wordmark__square{width:32px;height:32px}
  .card .wordmark__name{font-size:12.5px}
  .card__holder{position:absolute;right:22px;top:80px;text-align:right;color:var(--brand-blue);font-weight:700;font-size:12px}
  .card__holder small{display:block;color:var(--brand-red);font-weight:400;font-size:7.5px}
  .card .footer-band{height:100px}
  .card .contact{left:20px;top:45px;font-size:8px;gap:3px}
  .card .contact svg{width:9px;height:9px;margin-right:6px}
  .card .contact--web{left:253px;top:55px}
</style>
</head>
<body>

<svg class="icon-defs" aria-hidden="true">
  <symbol id="i-pin" viewBox="0 0 16 16"><path d="M8 1a5 5 0 0 0-5 5c0 3.6 5 9 5 9s5-5.4 5-9a5 5 0 0 0-5-5zm0 7a2 2 0 1 1 0-4 2 2 0 0 1 0 4z"/></symbol>
  <symbol id="i-phone" viewBox="0 0 16 16"><path d="M1 5c0-2 3-3 7-3s7 1 7 3v1h-4V4.5C10 4 6 4 5 4.5V6H1zM4 7h8l2 5v2H2v-2zm4 1.5a2 2 0 1 0 0 4 2 2 0 0 0 0-4z"/></symbol>
  <symbol id="i-box" viewBox="0 0 16 16"><path d="M2 4h12v8H2zM1 6h1v4H1zm13 0h1v4h-1zM4 6v4h3V6zm5 0v1h3V6zm0 2v1h3V8z"/></symbol>
  <symbol id="i-mail" viewBox="0 0 16 16"><path d="M1 3h14v10H1zm1.5 1.5L8 9l5.5-4.5v-.5h-11zm0 2V12h11V6.5L8 11z"/></symbol>
  <symbol id="i-web" viewBox="0 0 16 16"><path d="M8 1a7 7 0 1 0 0 14A7 7 0 0 0 8 1zm0 1.4c.8.8 1.5 2.2 1.8 3.6H6.2C6.5 4.6 7.2 3.2 8 2.4zM2.6 7h2.9a12 12 0 0 0 0 2H2.6a5.6 5.6 0 0 1 0-2zm.5 3h2.6c.2 1.3.6 2.4 1.1 3.2A5.6 5.6 0 0 1 3.1 10zm0-4a5.6 5.6 0 0 1 3.7-3.2C6.3 3.6 5.9 4.7 5.7 6zM8 13.6c-.8-.8-1.5-2.2-1.8-3.6h3.6c-.3 1.4-1 2.8-1.8 3.6zM6.5 9a11 11 0 0 1 0-2h3a11 11 0 0 1 0 2zm2.7 4.2c.5-.8.9-1.900 1.1-3.2h2.6a5.6 5.6 0 0 1-3.7 3.2zM10.5 9a12 12 0 0 0 0-2h2.9a5.6 5.6 0 0 1 0 2zm-.2-3c-.2-1.3-.6-2.4-1.1-3.2A5.6 5.6 0 0 1 12.9 6z"/></symbol>
</svg>

<!-- letterhead, second sheet -->
<div class="letter-back"></div>

<!-- letterhead -->
<section class="sheet letterhead">
  <div class="wordmark">
    <span class="wordmark__square"></span>
    <span class="wordmark__name">Corla Penwick<br>Children's Foundation</span>
  </div>
  <p class="letterhead__mission">The MISSION of the CORLA PENWICK FOUNDATION is to provide after school enrichment, health, and fitness programs in a safe and nurturing environment</p>

  <aside class="board">
    <p class="board__title">Board of Directors:</p>
    <ul class="board__list">
      <li>Ada Marlow</li><li>Ben Okafor</li><li>Clara Voss</li><li>Dean Ruiz</li><li>Elle Hart</li>
      <li>Finn Dorsey</li><li>Gina Park</li><li>Hal Brenner</li><li>Iris Quade</li><li>Joel Amari</li>
      <li>Kara Lind</li><li>Leo Sutter</li><li>Mia Torres</li><li>Nate Pryce</li><li>Opal Greer</li>
      <li>Paul Kerr</li><li>Rosa Nyland</li><li>Sam Ortega</li><li>Tess Whalen</li><li>Vic Hollis</li>
      <li>Wren Alcott</li><li>Yara Dunn</li><li>Zeke Morrow</li><li>Abby Fenn</li><li>Cole Raskin</li>
      <li>Dana Pierce</li><li>Eli Strand</li><li>Faye Colton</li><li>Gus Harlan</li><li>Hope Vance</li>
      <li>Ivan Roche</li><li>June Tabor</li><li>Kurt Ellis</li><li>Lena Marsh</li><li>Milo Grant</li>
      <li>Nora Bright</li><li>Owen Casey</li><li>Pia Lowell</li><li>Reid Sloan</li><li>Sara Quinn</li>
      <li>Theo Baird</li><li>Uma Fields</li><li>Vera Kent</li><li>Wade Lyon</li>
    </ul>
  </aside>

  <article class="letter">
    <p class="letter__subject">Quisque mauris odio, ornare non aliquet eget, consequat quis sapien.</p>
    <p>Dear Sir,</p>
    <p>ullamcorper in varius risus consectetur. Suspendisse in est felis. Nam sodales egestas diam id interdum. Sed velit metus, congue ut lacinia sit amet, accumsan nec dui. Lorem ipsum dolor sit amet, consectetur adipiscing elit. In nisl orci, vehicula vel adipiscing in, feugiat a odio. Duis vestibulum mauris eget ipsum pellentesque dictum. Nulla ut turpis eros, nec tempus purus. Ut sodales libero ac sapien gravida condimentum. Curabitur urna tortor, cursus sit amet dictum eget, vehicula vel odio.</p>
    <p>Sed et quam velit. Nunc felis erat, sagittis eu pulvinar nec, placerat eget urna. Morbi aliquet, metus at imperdiet luctus, urna lectus condimentum erat, et convallis nisi sapien quis massa. Cras nec varius arcu. Fusce eget arcu eros, ut sodales elit. Nullam sagittis, erat eget placerat consectetur, ante magna euismod est, dapibus venenatis tortor erat vel justo. Sed tempor cursus suscipit. Aenean ac lacus eros. Class aptent taciti sociosqu ad litora torquent per conubia nostra, per inceptos himenaeos. Fusce viverra est eu mi consectetur quis ultricies dui cursus. Praesent ante est, aliquam ac malesuada et, convallis eleifend quam. Vestibulum ante ipsum primis in faucibus orci luctus et ultrices posuere cubilia Curae; Ut tellus augue, euismod sed vehicula eu, tempor fringilla sapien. Nulla nec lacus tellus.</p>
    <p>Morbi nec arcu eget justo imperdiet aliquam. Sed erat erat, pretium eu tincidunt sed, dapibus non orci. Suspendisse libero lorem, hendrerit et fermentum at, adipiscing a quam. Quisque justo leo, faucibus ac luctus a, facilisis vel elit. Nulla consequat metus a risus egestas eget lacinia elit semper. Nunc iaculis nisi ut urna condimentum aliquet cursus lacus hendrerit. Nunc ornare quam ut ipsum placerat eu tempor metus egestas. Integer vehicula quam id magna placerat vitae porta ante pharetra. Fusce vitae arcu at leo adipiscing interdum. Nunc vehicula, enim sed pretium malesuada, odio augue pellentesque risus, at eleifend neque diam et nunc. Suspendisse lorem felis, consectetur ut venenatis vitae, dictum eu diam. Sed in justo quis urna auctor aliquet. Fusce at nisi in velit eleifend accumsan.</p>
    <p>Aenean tempor fringilla euismod. Proin quis nisi enim. Nulla facilisi. Pellentesque fermentum quam non lacus laoreet eu hendrerit urna vulputate. Maecenas fermentum nunc ut nunc suscipit facilisis. Sed odio metus, rhoncus sed vehicula vitae, mattis ut arcu. Aenean nisl tellus, iaculis et facilisis tempor, vulputate ut nisi. Integer hendrerit, nisi sit amet tempor fringilla, dui ante scelerisque erat, at tristique ipsum velit tincidunt velit. Sed sagittis quam hendrerit metus posuere ornare. Maecenas quis auctor ante. In vitae ligula lacus. Cras blandit eleifend purus in gravida. Sed id risus tellus. Curabitur quis sem dui, at porta arcu.</p>
    <p class="letter__paragraph--joined">Aenean tempor fringilla euismod. Proin quis nisi enim. Nulla facilisi. Pellentesque fermentum quam non lacus laoreet eu hendrerit urna vulputate. Maecenas fermentum nunc ut nunc suscipit facilisis. Sed odio metus, rhoncus sed vehicula vitae, mattis ut arcu. Aenean nisl tellus, iaculis et facilisis tempor, vulputate ut nisi. Integer hendrerit, nisi sit amet tempor fringilla, dui ante scelerisque erat, at tristique ipsum velit tincidunt velit. Sed sagittis quam hendrerit metus posuere ornare. Maecenas quis auctor ante. In vitae ligula lacus. Cras blandit eleifend purus in gravida. Sed id risus tellus. Curabitur quis sem dui, at porta arcu.</p>
    <p class="letter__closing">Your's Faithfully,</p>
    <p class="letter__signer">Corla Penwick<small>Children's Foundation</small></p>
  </article>

  <div class="footer-band">
    <svg class="swoosh" viewBox="0 0 575 137" preserveAspectRatio="none" aria-hidden="true">
      <path d="M0 0 C120 30 330 48 575 18 L575 137 L0 137Z" fill="var(--brand-red)"/>
      <path d="M0 10 C150 45 360 50 575 30 C380 62 160 58 0 30Z" fill="#fff"/>
      <path d="M0 30 C160 58 380 62 575 30 L575 137 L0 137Z" fill="var(--brand-blue)"/>
    </svg>
    <div class="contact">
      <span class="contact__line"><svg><use href="#i-pin"/></svg>Alder Springs, Oregon 32917 USA</span>
      <span class="contact__line"><svg><use href="#i-phone"/></svg>877-(CPF)-2315</span>
      <span class="contact__line"><svg><use href="#i-box"/></svg>PO BOX 371924</span>
    </div>
    <div class="contact contact--web">
      <span class="contact__line"><svg><use href="#i-mail"/></svg>community@cpfyouth.org</span>
      <span class="contact__line"><svg><use href="#i-web"/></svg>www.cpfyouth.org</span>
    </div>
  </div>
</section>

<!-- envelope, flap side -->
<div class="envelope-back">
  <svg class="envelope-back__flap" viewBox="0 0 445 58" preserveAspectRatio="none" aria-hidden="true">
    <path d="M0 0H445V5L437 45Q434 58 420 58H25Q11 58 8 45L0 5Z" fill="var(--brand-blue)"/>
  </svg>
</div>

<!-- envelope, address side -->
<section class="sheet envelope">
  <div class="wordmark">
    <span class="wordmark__square"></span>
    <span class="wordmark__name">Corla Penwick<br>Children's Foundation</span>
  </div>
  <div class="envelope__window"></div>
  <div class="footer-band">
    <svg class="swoosh" viewBox="0 0 466 90" preserveAspectRatio="none" aria-hidden="true">
      <path d="M0 0 C100 20 270 34 466 12 L466 90 L0 90Z" fill="var(--brand-red)"/>
      <path d="M0 8 C120 30 290 36 466 22 C310 44 130 42 0 20Z" fill="#fff"/>
      <path d="M0 20 C130 42 310 44 466 22 L466 90 L0 90Z" fill="var(--brand-blue)"/>
    </svg>
    <div class="contact">
      <span class="contact__line"><svg><use href="#i-pin"/></svg>Alder Springs, Oregon 32917 USA</span>
      <span class="contact__line"><svg><use href="#i-phone"/></svg>877-(CPF)-2315</span>
      <span class="contact__line"><svg><use href="#i-box"/></svg>PO BOX 371924</span>
    </div>
    <div class="contact contact--web">
      <span class="contact__line"><svg><use href="#i-mail"/></svg>community@cpfyouth.org</span>
      <span class="contact__line"><svg><use href="#i-web"/></svg>www.cpfyouth.org</span>
    </div>
  </div>
</section>

<!-- business card, reverse -->
<section class="card-back">
  <p class="card-back__mission">The MISSION of the CORLA PENWICK FOUNDATION is to provide after<br>school enrichment, health, and fitness programs in a safe and nurturing environment</p>
</section>

<!-- business card, front -->
<section class="sheet card">
  <div class="wordmark">
    <span class="wordmark__square"></span>
    <span class="wordmark__name">Corla Penwick<br>Children's Foundation</span>
  </div>
  <p class="card__holder">Corla Penwick<small>Vice President</small></p>
  <div class="footer-band">
    <svg class="swoosh" viewBox="0 0 374 100" preserveAspectRatio="none" aria-hidden="true">
      <path d="M0 0 C80 22 220 36 374 14 L374 100 L0 100Z" fill="var(--brand-red)"/>
      <path d="M0 9 C100 32 240 38 374 24 C250 48 100 46 0 22Z" fill="#fff"/>
      <path d="M0 22 C100 46 250 48 374 24 L374 100 L0 100Z" fill="var(--brand-blue)"/>
    </svg>
    <div class="contact">
      <span class="contact__line"><svg><use href="#i-pin"/></svg>Alder Springs, Oregon 32917 USA</span>
      <span class="contact__line"><svg><use href="#i-phone"/></svg>877-(CPF)-2315</span>
      <span class="contact__line"><svg><use href="#i-box"/></svg>PO BOX 371924</span>
    </div>
    <div class="contact contact--web">
      <span class="contact__line"><svg><use href="#i-mail"/></svg>community@cpfyouth.org</span>
      <span class="contact__line"><svg><use href="#i-web"/></svg>www.cpfyouth.org</span>
    </div>
  </div>
</section>

</body>
</html>
```